Duel Business card

Want an edgy business card that shows both of our companies on each side of the card, OR both together with a cool design.

*Must be edgy: We have attached our two business logos. We are a bail bond and immigration bond company.

Would like the address on one side only.
Need Phone, cell, website, address, and Name

Company Name 1: Cellgate Release Partners
www.cellgatereleasepartners.example

Company Name 2: Borderline Surety Associates
www.borderlinesuretyassociates.example

These cards will need to be easily changeable so I can modify new employees

Target Market(s)

people in jail, takign imigrants out of jail and from being taken back to there country

Industry/Entity Type

Business

Requirements
Must have
• Include both logos attached

```html
<!DOCTYPE html>
<html lang="en">
<head>
<meta charset="utf-8">
<title>Cellgate Release Partners &amp; Borderline Surety Associates — Business Card</title>
<link rel="stylesheet" href="https://fonts.googleapis.com/css2?family=Lato:wght@300;400;700;900&display=swap">
<style>
  :root {
    --navy: #1d2a8c;
    --navy-deep: #16206e;
    --gold: #d9b21c;
    --red: #d3202a;
    --paper: #f4f4f2;
    --ink: #1d2a8c;
    --white: #ffffff;
    --backdrop: #e7e4de;
    --badge: #f1f1f1;
  }
  * { box-sizing: border-box; margin: 0; padding: 0; }
  html, body { width: 1200px; height: 720px; overflow: hidden; }
  body {
    background: var(--backdrop);
    font-family: "Lato", Arial, sans-serif;
    display: flex;
    align-items: center;
    justify-content: center;
    gap: 40px;
  }
  .card {
    position: relative;
    width: 540px;
    height: 308px;
    overflow: hidden;
    box-shadow: 0 6px 18px rgba(0,0,0,.18);
  }

  /* ---------- front ---------- */
  .card--front { background: var(--navy); }
  .front-head {
    position: absolute; inset: 0 0 auto 0;
    height: 128px;
    background: var(--paper);
    display: flex;
    align-items: center;
    justify-content: space-between;
    padding: 0 42px 0 60px;
  }
  .front-head::after {
    content: "";
    position: absolute; left: 0; right: 0; bottom: -8px;
    height: 8px;
    background: linear-gradient(var(--gold) 0 3px, var(--white) 3px 5px, var(--red) 5px 8px);
  }
  .brand {
    display: flex; align-items: center; gap: 10px;
    color: var(--ink);
    font-weight: 900;
    text-transform: uppercase;
    line-height: 1.05;
  }
  .brand__dot {
    flex: none;
    width: 30px; height: 30px;
    border-radius: 50%;
    background: var(--gold);
  }
  .brand__name { font-size: 15px; letter-spacing: .5px; }
  .seal { display: flex; align-items: center; gap: 10px; }
  .seal__disc {
    flex: none;
    width: 70px; height: 70px;
    border-radius: 50%;
    background: var(--badge);
    border: 3px solid #cfcfcf;
  }
  .seal__name {
    color: var(--red);
    font-weight: 900;
    font-size: 11px;
    text-transform: uppercase;
    line-height: 1.15;
    width: 92px;
  }
  .holder {
    position: absolute; top: 150px; left: 0; right: 0;
    text-align: center;
    color: var(--white);
    font-weight: 400;
    font-size: 25px;
  }
  .contact {
    position: absolute; bottom: 30px;
    color: var(--white);
    font-size: 12.5px;
    line-height: 1.45;
  }
  .contact--direct { left: 22px; }
  .contact--office { right: 24px; }
  .contact li { list-style: none; display: flex; align-items: center; gap: 12px; }
  .contact svg { width: 12px; height: 13px; flex: none; }

  /* ---------- back ---------- */
  .card--back { background: var(--navy); }
  .ribbon {
    position: absolute;
    height: 24px;
    display: flex; align-items: center;
    font-size: 11.5px;
    color: var(--white);
  }
  .ribbon--gold {
    top: 30px; right: 0; width: 300px;
    background: var(--gold);
    clip-path: polygon(10px 0, 100% 0, 100% 100%, 10px 100%, 0 50%);
    padding-left: 24px;
  }
  .ribbon--red {
    top: 206px; left: 0; width: 350px;
    background: var(--red);
    clip-path: polygon(0 0, calc(100% - 12px) 0, 100% 50%, calc(100% - 12px) 100%, 0 100%);
    padding-left: 30px;
  }
  .card--back .brand {
    position: absolute; left: 48px; top: 106px;
    color: var(--white);
  }
  .card--back .brand__name { font-size: 20px; }
  .card--back .brand__dot { width: 40px; height: 40px; }
  .card--back .seal {
    position: absolute; right: 36px; top: 74px;
    flex-direction: column; gap: 8px;
  }
  .card--back .seal__disc { width: 96px; height: 96px; }
  .card--back .seal__name {
    color: var(--white);
    width: 130px;
    text-align: center;
  }
</style>
</head>
<body>

  <section class="card card--front" aria-label="Card front">
    <header class="front-head">
      <div class="brand">
        <span class="brand__dot"></span>
        <span class="brand__name">Cellgate<br>Release Partners</span>
      </div>
      <div class="seal">
        <span class="seal__disc"></span>
        <span class="seal__name">Borderline Surety Associates</span>
      </div>
    </header>

    <h1 class="holder">Rowan Pellham</h1>

    <ul class="contact contact--direct">
      <li>
        <svg viewBox="0 0 12 13" aria-hidden="true"><rect x=".5" y=".5" width="11" height="12" rx="1.5" fill="none" stroke="#d9b21c"/><rect x="3" y="3" width="6" height="3" fill="#d9b21c"/><circle cx="4" cy="9" r="1" fill="#d9b21c"/><circle cx="8" cy="9" r="1" fill="#d9b21c"/></svg>
        0155 862 4471 ext 2210
      </li>
      <li>
        <svg viewBox="0 0 12 13" aria-hidden="true"><rect x="2" y=".5" width="8" height="12" rx="1.5" fill="none" stroke="#d9b21c"/><rect x="3.5" y="2" width="5" height="6" fill="#d9b21c"/><circle cx="6" cy="10.5" r=".9" fill="#d9b21c"/></svg>
        rowan.pellham@cellgate.example
      </li>
    </ul>

    <ul class="contact contact--office">
      <li>www.cellgate.example</li>
      <li>Unit 4, Harbour Row, Millbrook, MB3 7QT</li>
    </ul>
  </section>

  <section class="card card--back" aria-label="Card back">
    <div class="ribbon ribbon--gold">www.cellgatereleasepartners.example</div>

    <div class="brand">
      <span class="brand__dot"></span>
      <span class="brand__name">Cellgate<br>Release Partners</span>
    </div>

    <div class="seal">
      <span class="seal__disc"></span>
      <span class="seal__name">Borderline Surety Associates</span>
    </div>

    <div class="ribbon ribbon--red">www.borderlinesuretyassociates.example</div>
  </section>

</body>
</html>
```